BriskTail Pet - Cat Snack Range Packaging Design

Cat Velvo is a tasty snack for pets that comes in 3 flavors: Salmon, Tuna, Chicken. Each pack has 5 sticks.

Designs are currently too "cartoon-ish"; looking to refresh design into a high-end, "professional" product.

Prefer to have black/dark background with different colors for each flavor, but also open to designers' own creative take, as long as product looks professional.

Can refer to cat food brand "Marlow Feline" and "Plim" photo attached for reference.
https://www.marlowfeline.example/us/cats/products/vet-products

Looking to expand the design concept in the future to a whole range of cat products, such as cat litter, dental chewing sticks, canned cat food, etc.

Target Market(s)

More premium, high-end pet owners

Colors

Designer to choose only greyscale colors for use in the design.

Requirements
Must have
• Professional look
Nice to have
• Design template that can be copied and used for various product ranges (cat snacks, cans, litter, etc)

```html
<!DOCTYPE html>
<html lang="en">
<head>
<meta charset="UTF-8">
<title>BriskTail Pet – Cat Velvo Chicken Mini Pouch</title>
<link href="https://fonts.googleapis.com/css2?family=Montserrat:wght@600;700;800&family=Kalam:wght@700&display=swap" rel="stylesheet">
<style>
  :root{
    --backdrop:#f5ece4;
    --pack-dark:#262324;
    --accent:#d8998c;
    --accent-deep:#c98577;
    --window:#9b9b9b;
    --ink-light:#f4f1ee;
    --art-fur-a:#6d6a67;
    --art-fur-b:#2f2c2b;
    --mascot-a:#e9e4df;
    --mascot-b:#9a9088;
  }
  *{margin:0;padding:0;box-sizing:border-box}
  html,body{width:1200px;height:900px;overflow:hidden}
  body{background:var(--backdrop);position:relative;font-family:"Montserrat",sans-serif;color:var(--ink-light)}

  /* ---------- Front pouch ---------- */
  .pouch{position:absolute;left:250px;top:108px;width:356px;height:684px}
  .pouch-shape{position:absolute;inset:0}
  .pouch-mascot{position:absolute;left:134px;top:78px;width:86px;height:90px;border-radius:46% 46% 40% 40%;
    background:radial-gradient(circle at 50% 40%,var(--mascot-a),var(--mascot-b))}
  .brand-name{position:absolute;left:0;right:0;top:176px;text-align:center;font-weight:700;font-size:19px;letter-spacing:.5px;color:var(--ink-light)}
  .product-name{position:absolute;left:0;right:0;top:208px;text-align:center;font-weight:800;font-size:40px;letter-spacing:1px;color:var(--ink-light);line-height:1}
  .tagline{position:absolute;left:0;right:0;top:262px;text-align:center;font-family:"Kalam",cursive;font-size:12px;letter-spacing:.4px}
  .flavour{position:absolute;left:0;right:0;top:298px;text-align:center;font-weight:800;font-size:24px;color:var(--accent);letter-spacing:.5px;line-height:1}
  .flavour-note{position:absolute;left:0;right:0;top:330px;text-align:center;font-family:"Kalam",cursive;font-size:13px;letter-spacing:.3px}
  .pouch-cat{position:absolute;left:150px;top:378px;width:150px;height:284px;border-radius:45% 45% 18% 18%;
    background:linear-gradient(180deg,var(--art-fur-a),var(--art-fur-b))}
  .natural-badge{position:absolute;left:12px;top:592px;width:34px;height:34px}
  .natural-label{position:absolute;left:8px;top:634px;font-weight:800;font-size:9px;color:var(--ink-light)}
  .flavour-icon{position:absolute;left:72px;top:588px;width:54px;height:62px;border-radius:40% 40% 20% 20%;
    background:linear-gradient(180deg,var(--ink-light),#d9d4cf);opacity:.9}
  .net-weight{position:absolute;left:6px;top:662px;font-weight:600;font-size:10px;color:var(--ink-light)}

  /* ---------- Single stick ---------- */
  .stick{position:absolute;width:440px;height:60px;background:var(--pack-dark);
    border-top:6px solid var(--accent);border-bottom:9px solid var(--accent)}
  .stick-vertical{left:508px;top:300px;transform:translate(220px,0) rotate(90deg);transform-origin:center}
  .stick-horizontal{left:650px;top:640px}
  .stick-mascot{position:absolute;left:14px;top:3px;width:30px;height:22px;border-radius:45%;
    background:radial-gradient(circle at 50% 40%,var(--mascot-a),var(--mascot-b))}
  .stick-brand{position:absolute;left:4px;top:25px;width:52px;text-align:center;font-weight:700;font-size:6.5px;white-space:nowrap}
  .stick-product{position:absolute;left:62px;top:6px;font-weight:800;font-size:7px;white-space:nowrap}
  .stick-tagline{position:absolute;left:62px;top:16px;font-family:"Kalam",cursive;font-size:5px;white-space:nowrap}
  .stick-flavour{position:absolute;left:118px;top:5px;font-weight:800;font-size:21px;color:var(--accent);white-space:nowrap;line-height:1}
  .stick-note{position:absolute;left:122px;top:28px;font-family:"Kalam",cursive;font-size:10px;white-space:nowrap;line-height:1}
  .stick-icons{position:absolute;left:372px;top:10px;width:30px;height:26px}
  .stick-cat{position:absolute;right:4px;top:2px;width:28px;height:40px;border-radius:40% 40% 15% 15%;
    background:linear-gradient(180deg,var(--art-fur-a),var(--art-fur-b))}
</style>
</head>
<body>

<section class="pouch" aria-label="Cat Velvo chicken mini pouch front">
  <svg class="pouch-shape" viewBox="0 0 356 684" width="356" height="684" aria-hidden="true">
    <defs>
      <clipPath id="pouch-clip"><path d="M14 0 H342 Q356 0 356 14 V684 H0 V14 Q0 0 14 0 Z"/></clipPath>
    </defs>
    <g clip-path="url(#pouch-clip)">
      <rect width="356" height="684" fill="var(--pack-dark)"/>
      <path d="M68 368 H356 V600 H68 Q68 480 68 368 Z" fill="var(--window)"/>
      <path d="M0 545 C90 520 180 470 250 430 C300 400 340 385 356 378 V684 H0 Z" fill="var(--accent)"/>
    </g>
    <rect x="150" y="14" width="56" height="16" rx="8" fill="var(--backdrop)"/>
  </svg>

  <div class="pouch-mascot" role="img" aria-label="Brand mascot illustration"></div>
  <div class="brand-name">BriskTail Pet</div>
  <h1 class="product-name">CAT VELVO</h1>
  <p class="tagline">HEALTHY, TASTY &amp; NATURAL!</p>
  <h2 class="flavour">CHICKEN MINI POUCH</h2>
  <p class="flavour-note">WITH EXTRA-ADDED CAT GRASS</p>

  <div class="pouch-cat" role="img" aria-label="Photo of a seated long-haired tabby cat"></div>

  <svg class="natural-badge" viewBox="0 0 34 34" aria-hidden="true">
    <circle cx="17" cy="17" r="15" fill="none" stroke="var(--ink-light)" stroke-width="2"/>
    <path d="M11 23 C11 14 17 10 24 10 C24 18 19 23 11 23 Z M11 23 L19 15" fill="none" stroke="var(--ink-light)" stroke-width="2" stroke-linejoin="round"/>
  </svg>
  <span class="natural-label">NATURAL</span>
  <div class="flavour-icon" role="img" aria-label="Chicken illustration"></div>
  <span class="net-weight">NET: 75 G (15G X 5)</span>
</section>

<section class="stick stick-vertical" aria-label="Single stick, standing">
  <div class="stick-mascot" role="img" aria-label="Brand mascot illustration"></div>
  <div class="stick-brand">BriskTail Pet</div>
  <div class="stick-product">CAT VELVO</div>
  <div class="stick-tagline">HEALTHY &amp; TASTY</div>
  <div class="stick-flavour">CHICKEN MINI POUCH</div>
  <div class="stick-note">WITH EXTRA-ADDED CAT GRASS</div>
  <svg class="stick-icons" viewBox="0 0 30 26" aria-hidden="true">
    <circle cx="8" cy="9" r="6" fill="none" stroke="var(--ink-light)" stroke-width="1.2"/>
    <path d="M5 12 C5 8 8 6 11 6 C11 10 9 12 5 12 Z" fill="none" stroke="var(--ink-light)" stroke-width="1"/>
    <circle cx="22" cy="14" r="5" fill="none" stroke="var(--ink-light)" stroke-width="1.2"/>
  </svg>
  <div class="stick-cat" role="img" aria-label="Photo of a tabby cat"></div>
</section>

<section class="stick stick-horizontal" aria-label="Single stick, lying">
  <div class="stick-mascot" role="img" aria-label="Brand mascot illustration"></div>
  <div class="stick-brand">BriskTail Pet</div>
  <div class="stick-product">CAT VELVO</div>
  <div class="stick-tagline">HEALTHY &amp; TASTY</div>
  <div class="stick-flavour">CHICKEN MINI POUCH</div>
  <div class="stick-note">WITH EXTRA-ADDED CAT GRASS</div>
  <svg class="stick-icons" viewBox="0 0 30 26" aria-hidden="true">
    <circle cx="8" cy="9" r="6" fill="none" stroke="var(--ink-light)" stroke-width="1.2"/>
    <path d="M5 12 C5 8 8 6 11 6 C11 10 9 12 5 12 Z" fill="none" stroke="var(--ink-light)" stroke-width="1"/>
    <circle cx="22" cy="14" r="5" fill="none" stroke="var(--ink-light)" stroke-width="1.2"/>
  </svg>
  <div class="stick-cat" role="img" aria-label="Photo of a tabby cat"></div>
</section>

</body>
</html>
```